Veterinary Hospital Business Card

We have recently updated our logo and wish to have a business card designed incorporating the new look and flow. We are a full service veterinary hospital also offering laser therapy, boarding, and grooming. Our website is www.marlowpaws.com

Industry/Entity Type

Veterinary

```html
<!DOCTYPE html>
<html lang="en">
<head>
<meta charset="utf-8">
<title>Marlow Animal Hospital – Business Card</title>
<link rel="stylesheet" href="https://fonts.googleapis.com/css2?family=Patrick+Hand&display=swap">
<style>
  :root {
    --navy-deep: #0a2140;
    --navy-mid: #12365f;
    --card-blue: #3a80a6;
    --card-blue-dark: #2f6f95;
    --icon-blue: #0d3a7e;
    --logo-blue: #7fc4d6;
    --text-white: #ffffff;
  }
  html, body {
    margin: 0;
    padding: 0;
    width: 667px;
    height: 1200px;
    overflow: hidden;
    background: #ffffff;
  }
  .card {
    position: relative;
    width: 667px;
    height: 1200px;
    overflow: hidden;
    background: var(--card-blue);
    font-family: "Patrick Hand", "Comic Sans MS", cursive;
    color: var(--text-white);
  }
  .card-header {
    position: absolute;
    left: -140px;
    top: -320px;
    width: 947px;
    height: 710px;
    border-radius: 50%;
    background: radial-gradient(ellipse at 50% 62%, var(--navy-deep) 0%, var(--navy-mid) 55%, #1c4d78 80%, var(--card-blue) 100%);
  }
  .brand {
    position: absolute;
    top: 92px;
    left: 0;
    width: 667px;
    display: flex;
    align-items: center;
    justify-content: center;
    gap: 26px;
  }
  .brand-mark {
    width: 118px;
    height: 118px;
    border-radius: 50%;
    background: var(--logo-blue);
    flex: none;
  }
  .brand-name {
    margin: 0;
    font-size: 62px;
    line-height: 0.95;
    font-weight: 400;
    color: var(--logo-blue);
    letter-spacing: 1px;
  }
  .holder-name {
    position: absolute;
    top: 398px;
    left: 0;
    width: 667px;
    margin: 0;
    text-align: center;
    font-size: 74px;
    font-weight: 400;
    line-height: 1;
  }
  .paw-trail {
    position: absolute;
    left: 30px;
    width: 607px;
    height: 92px;
    border-radius: 46px;
    background: linear-gradient(90deg, var(--card-blue-dark), #2a6890 50%, var(--card-blue-dark));
  }
  .paw-trail--upper { top: 526px; }
  .paw-trail--lower { top: 1060px; }
  .contact-list {
    position: absolute;
    top: 686px;
    left: 0;
    margin: 0;
    padding: 0;
    list-style: none;
  }
  .contact-item {
    position: relative;
    padding-left: 110px;
    font-size: 37px;
    line-height: 65px;
    white-space: nowrap;
  }
  .contact-icon {
    position: absolute;
    left: 22px;
    top: 13px;
    width: 40px;
    height: 40px;
  }
</style>
</head>
<body>
<main class="card">
  <div class="card-header"></div>

  <div class="brand">
    <span class="brand-mark"></span>
    <p class="brand-name">MARLOW<br>ANIMAL<br>HOSPITAL</p>
  </div>

  <h1 class="holder-name">Jane Marsh</h1>

  <div class="paw-trail paw-trail--upper" role="img" aria-label="Trail of paw prints"></div>

  <ul class="contact-list">
    <li class="contact-item">
      <svg class="contact-icon" viewBox="0 0 40 40" aria-hidden="true">
        <circle cx="20" cy="20" r="19" fill="var(--icon-blue)"/>
        <path d="M10 20 L20 11 L30 20 M13 18 V29 H27 V18" fill="none" stroke="#9ec9e0" stroke-width="2.6" stroke-linejoin="round"/>
      </svg>
      1180 Marlow Rd
    </li>
    <li class="contact-item">Fairbrook, SC, 29810</li>
    <li class="contact-item">
      <svg class="contact-icon" viewBox="0 0 40 40" aria-hidden="true">
        <circle cx="20" cy="20" r="19" fill="var(--icon-blue)"/>
        <path d="M13 11 L17 11 L19 16 L16.5 18 C18 21 20 23 22 24 L24 21.5 L29 23.5 L29 27 C29 28.5 27.5 29.5 26 29 C19 27 13 21 11 14 C10.5 12.5 11.5 11 13 11 Z" fill="#9ec9e0"/>
      </svg>
      (803) 555-0147
    </li>
    <li class="contact-item">
      <svg class="contact-icon" viewBox="0 0 40 40" aria-hidden="true">
        <circle cx="20" cy="20" r="19" fill="var(--icon-blue)"/>
        <text x="20" y="27" text-anchor="middle" font-family="Arial, sans-serif" font-size="21" fill="#9ec9e0">@</text>
      </svg>
      clientcare@marlowpaws.com
    </li>
    <li class="contact-item">
      <svg class="contact-icon" viewBox="0 0 40 40" aria-hidden="true">
        <circle cx="20" cy="20" r="19" fill="var(--icon-blue)"/>
        <g fill="none" stroke="#9ec9e0" stroke-width="1.8">
          <circle cx="20" cy="20" r="11"/>
          <ellipse cx="20" cy="20" rx="5" ry="11"/>
          <line x1="9" y1="20" x2="31" y2="20"/>
          <line x1="11" y1="14" x2="29" y2="14"/>
          <line x1="11" y1="26" x2="29" y2="26"/>
        </g>
      </svg>
      www.marlowpaws.com
    </li>
  </ul>

  <div class="paw-trail paw-trail--lower" role="img" aria-label="Trail of paw prints"></div>
</main>
</body>
</html>
```